Quendra - Clear Spirit Cosmetics

Please design a logo and business cards for new food supplements, cosmetics and herbal fixatives. The products are produced ecologically and biologically in the South Tyrol and Trentino alps. The products are pure and noble. Quendra = pure vitality Colors Background: dark or black matt (soft touch) Logodesign: powerful, elegant, violet with glossy foil The logo and design should convey warmth, passion and the 6th sense, you should get the impression that you can smell the herbal odor , Logo and business cards for new food supplements, cosmetics and herbal fixatives. The products are produced ecologically and biologically in the South Tyrol and Trentino alps. The products are pure and noble. Quendra = pure vitality Colors Background: dark or black matt (softtouch) Logodesign: powerful elegant violet with glossy foil The logo and design is meant to convey warmth, passion and the 6th sense, you should get the impression that you can smell the herbal perfume.

Target Market(s)

Food, food supplements, vitality, health

Contact Information for Business Card

Please provide an elegant darf design that is puristic, but has a very good logo design
Elegantes dunkles design, puristisch

Logo Text

Quendra - clear Spirit

Colors
6b449b

Requirements
Must have
• SVG Files Alpha channel for foil embossing High-quality design
Nice to have
• Pure elegance
Should not have
• to colorful colors

```html
<!DOCTYPE html>
<html lang="en">
<head>
<meta charset="utf-8">
<title>Quendra - Clear Spirit Cosmetics · Business Card</title>
<link rel="stylesheet" href="https://fonts.googleapis.com/css2?family=Montserrat:wght@300;400;500&display=swap">
<style>
  :root {
    --stage: #d3d3d5;
    --card: #161616;
    --violet: #7a4cad;
    --violet-soft: #7d58ad;
    --violet-icon: #6b449b;
    --icon-ink: #161616;
    --shade: rgba(255,255,255,0.06);
  }
  * { margin: 0; padding: 0; box-sizing: border-box; }
  html, body {
    width: 1200px; height: 1000px; overflow: hidden;
    background: var(--stage);
    font-family: "Montserrat", sans-serif;
  }
  .canvas { position: relative; width: 1200px; height: 1000px; }
  .card {
    position: absolute; left: 262px; width: 675px; height: 383px;
    background: var(--card); border-radius: 36px; overflow: hidden;
  }
  .card--front { top: 100px; }
  .card--back { top: 520px; }

  .wordmark {
    position: absolute; color: var(--violet);
    font-weight: 400; line-height: 1; white-space: nowrap;
  }
  .card--front .wordmark {
    left: 0; right: 0; top: 138px; text-align: center;
    font-size: 104px; letter-spacing: 1px;
  }
  .card--back .wordmark {
    left: 28px; top: 52px; font-size: 60px;
  }

  .backdrop-mark {
    position: absolute; left: 312px; top: 28px; width: 340px; height: 330px;
    border-radius: 50%;
    background: radial-gradient(circle, rgba(255,255,255,0.09) 0%, rgba(255,255,255,0.04) 55%, rgba(255,255,255,0) 72%);
  }

  .identity { position: absolute; right: 25px; top: 34px; text-align: right; color: var(--violet-soft); }
  .identity__name { font-size: 30px; font-weight: 400; letter-spacing: 1px; line-height: 1.2; }
  .identity__role { font-size: 19px; font-weight: 400; letter-spacing: 1.2px; margin-top: 4px; }

  .contacts { position: absolute; top: 288px; display: flex; flex-direction: column; gap: 8px; }
  .contacts--left { left: 26px; }
  .contacts--right { right: 25px; }
  .contact { display: flex; align-items: center; gap: 10px; height: 30px;
    color: var(--violet-soft); font-size: 20.5px; font-weight: 400; letter-spacing: 0.3px; }
  .contact__icon { width: 30px; height: 30px; flex: none; }
</style>
</head>
<body>
<div class="canvas">

  <section class="card card--front">
    <div class="wordmark">Quendra</div>
  </section>

  <section class="card card--back">
    <div class="backdrop-mark" role="img" aria-label="Faint large brand emblem decoration"></div>

    <div class="wordmark">Quendra</div>

    <div class="identity">
      <div class="identity__name">Your Name</div>
      <div class="identity__role">Founder</div>
    </div>

    <div class="contacts contacts--left">
      <div class="contact">
        <svg class="contact__icon" viewBox="0 0 30 30" aria-hidden="true">
          <circle cx="15" cy="15" r="15" fill="var(--violet-icon)"/>
          <path d="M8 12c0-2 3-3 7-3s7 1 7 3v1.5h-3.5V12h-7v1.5H8z" fill="var(--icon-ink)"/>
          <path d="M10 14.5h10l1 6H9z" fill="var(--icon-ink)"/>
          <circle cx="15" cy="17.5" r="1.6" fill="var(--violet-icon)"/>
        </svg>
        <span>+12 345 678 910</span>
      </div>
      <div class="contact">
        <svg class="contact__icon" viewBox="0 0 30 30" aria-hidden="true">
          <circle cx="15" cy="15" r="15" fill="var(--violet-icon)"/>
          <rect x="10.5" y="7.5" width="9" height="15" rx="1.5" fill="var(--icon-ink)"/>
          <rect x="12" y="9.5" width="6" height="9" fill="var(--violet-icon)"/>
          <circle cx="15" cy="20.5" r="0.9" fill="var(--violet-icon)"/>
        </svg>
        <span>+12 345 678 910</span>
      </div>
    </div>

    <div class="contacts contacts--right">
      <div class="contact">
        <svg class="contact__icon" viewBox="0 0 30 30" aria-hidden="true">
          <circle cx="15" cy="15" r="15" fill="var(--violet-icon)"/>
          <rect x="8.5" y="10" width="13" height="10" rx="1" fill="var(--icon-ink)"/>
          <path d="M9 11l6 5 6-5" fill="none" stroke="var(--violet-icon)" stroke-width="1.3"/>
        </svg>
        <span>info@quendra.com</span>
      </div>
      <div class="contact">
        <svg class="contact__icon" viewBox="0 0 30 30" aria-hidden="true">
          <circle cx="15" cy="15" r="15" fill="var(--violet-icon)"/>
          <path d="M10 21L19 12" stroke="var(--icon-ink)" stroke-width="3" stroke-linecap="round"/>
          <path d="M13 9.5h8.5V18z" fill="var(--icon-ink)"/>
        </svg>
        <span>www.quendra.com</span>
      </div>
    </div>
  </section>

</div>
</body>
</html>
```